regPersonal Trainer Flyer Design

Reason: I have been very busy with other work and would like to extend the deadline to offer designers the chance to edit and improve designs with my help. Thank you for all the designs that have been sent so far.

```html
<!DOCTYPE html>
<html lang="en">
<head>
<meta charset="utf-8">
<title>Rowan Hale – Personal Trainer Flyer</title>
<link rel="stylesheet" href="https://fonts.googleapis.com/css2?family=Open+Sans:ital,wght@0,300;0,400;0,700;0,800;1,300&display=swap">
<style>
  :root {
    --ink: #333335;
    --brand-blue: #1a9ad6;
    --band-blue: #1b9bd8;
    --stripe-dark: #3a3a3c;
    --photo-light: #7fb0d8;
    --photo-deep: #1c4f8c;
    --band-grey-light: #f2f2f2;
    --band-grey-dark: #c9c9c9;
    --paper: #ffffff;
  }
  * { margin: 0; padding: 0; box-sizing: border-box; }
  html, body { width: 1200px; height: 1000px; overflow: hidden; background: var(--paper); }
  body { font-family: "Open Sans", Arial, sans-serif; color: var(--ink); }
  .flyer { position: relative; width: 1200px; height: 1000px; }

  .hero-art { position: absolute; left: 0; top: 0; }

  .brand-mark { position: absolute; left: 257px; top: 725px; width: 100px; text-align: center; }
  .brand-mark__name { font-size: 17px; font-weight: 400; color: var(--brand-blue); line-height: 1; display: block; }
  .brand-mark__tag { font-size: 6.5px; letter-spacing: 0.4px; color: #555; display: block; margin-top: 2px; }
  .brand-mark__square { width: 26px; height: 26px; background: var(--stripe-dark); margin: 0 auto 6px; }

  .trainer-title { position: absolute; right: 284px; top: 254px; text-align: right; }
  .trainer-title__name { font-size: 35px; font-weight: 300; line-height: 1.1; color: var(--ink); }
  .trainer-title__role { font-size: 20px; font-weight: 400; color: var(--brand-blue); line-height: 1.2; }

  .pain-points { position: absolute; left: 668px; top: 354px; list-style: none; }
  .pain-points li { font-size: 21px; font-style: italic; font-weight: 300; line-height: 26px; color: var(--ink); position: relative; padding-left: 20px; }
  .pain-points li::before { content: ""; position: absolute; left: 2px; top: 11px; width: 7px; height: 7px; border-radius: 50%; background: var(--brand-blue); }

  .benefits { position: absolute; right: 266px; top: 469px; text-align: right; font-size: 16px; line-height: 21.5px; color: var(--brand-blue); font-weight: 400; }

  .offer { position: absolute; left: 665px; top: 619px; width: 292px; }
  .offer__label { background: var(--band-blue); color: #fff; font-weight: 700; font-size: 19px; line-height: 24px; text-align: right; padding-right: 14px; }
  .offer__body { margin-left: 7px; background: linear-gradient(90deg, var(--band-grey-light), var(--band-grey-dark)); height: 51px; text-align: right; padding-right: 14px; }
  .offer__lead { font-size: 18px; line-height: 20px; color: var(--ink); padding-top: 2px; }
  .offer__headline { font-size: 30px; font-weight: 700; color: var(--brand-blue); line-height: 28px; }

  .contact { position: absolute; right: 262px; top: 700px; text-align: right; }
  .contact__phone { font-size: 26px; font-weight: 700; color: var(--ink); line-height: 32px; }
  .contact__email { font-size: 14px; color: var(--brand-blue); line-height: 18px; }
</style>
</head>
<body>
<main class="flyer">
  <svg class="hero-art" width="1200" height="1000" viewBox="0 0 1200 1000">
    <defs>
      <linearGradient id="photoTone" x1="0" y1="0" x2="1" y2="1">
        <stop offset="0" stop-color="var(--photo-light)"/>
        <stop offset="0.6" stop-color="#3c78b4"/>
        <stop offset="1" stop-color="var(--photo-deep)"/>
      </linearGradient>
    </defs>
    <polygon role="img" aria-label="Photograph of the personal trainer coaching a client through a barbell squat, with a blue-tinted portrait behind"
      points="243,232 480,232 545,390 500,460 610,768 375,768 243,420" fill="url(#photoTone)"/>
    <polygon class="chevron-stripe" points="472,232 510,232 568,390 530,460 645,768 607,768 498,460 545,390" fill="var(--stripe-dark)"/>
  </svg>

  <div class="brand-mark">
    <div class="brand-mark__square"></div>
    <span class="brand-mark__name">RowanHale</span>
    <span class="brand-mark__tag">HEALTH &amp; FITNESS</span>
  </div>

  <header class="trainer-title">
    <h1 class="trainer-title__name">Rowan Hale</h1>
    <p class="trainer-title__role">Personal Trainer</p>
  </header>

  <ul class="pain-points">
    <li>Lacking motivation?</li>
    <li>Not achieving your goals?</li>
    <li>Need help?</li>
    <li>Bored of the gym?</li>
  </ul>

  <p class="benefits">You're never too old<br>I can help improve your health<br>and well-being<br>Training can be at your home</p>

  <section class="offer">
    <div class="offer__label">INTRODUCTORY OFFER</div>
    <div class="offer__body">
      <p class="offer__lead">contact me now for</p>
      <p class="offer__headline">one free session</p>
    </div>
  </section>

  <address class="contact" style="font-style:normal">
    <p class="contact__phone">07700 900123</p>
    <p class="contact__email">rowanhale@example.co.uk</p>
  </address>
</main>
</body>
</html>
```